TRVL-NINE Web Design

We are a Health, Safety, Environmental & Quality Recruitment Agency, our clients are major corporate Mining, Oil & Gas and Engineering companies. We have offices in Perth & Melbourne, Australia

The website should be very functional & easy to navigate

BUT REALLY LOOKING FOR WOW FACTOR!

Please Note: TRVL CORPORATE IS OUR OLD COMPANY THE NEW ONE IS "TRVL-NINE" 

Some idea's from our competitors:

http://www.guardlinepeak.com.au/
http://www.vantagehiring.com.au/
http://www.brightpick.com.au/
http://www.kovastaffing.co.uk/
http://www.jobmarrow.com/health-safety-environment-jobs

Would love to see some of our valued clients and there logos

still looking for wow factor

Industry/Entity Type

Mining

Requirements
Must have
• A place where candidates can upload there resumes & other contact details
• eg: http://www.guardlinepeak.com.au/candidates/register-your-resume/
• A place we can load jobs on to eg: http://www.guardlinepeak.com.au/vacancies/
• Contact details:
• Perth: 12 Kestrel Ave, West Perth, Western Australia 6005
• t: 08 7153 4406 | f: 08 7153 4470 |
• Melbourne: Level 1, 218 Arbour Lane, Melbourne, Victoria 3000
• t: 03 6214 5072| f: 03 6231 4095 |
• e: dennisk@trvlnine.com.au | w: http://www.trvlnine.com.au

```html
<!DOCTYPE html>
<html lang="en">
<head>
<meta charset="utf-8">
<title>TRVL-NINE | Health, Safety, Environment &amp; Quality Recruitment</title>
<link rel="stylesheet" href="https://fonts.googleapis.com/css2?family=Arimo:wght@400;700&family=Open+Sans:wght@400&family=Questrial&display=swap">
<style>
  :root {
    --nav-bg: #3b3b3b;
    --nav-text: #c9c9c9;
    --nav-active: #3cc3dd;
    --white: #ffffff;
    --hero-top: #0b1a3c;
    --hero-mid: #1d3d78;
    --hero-glow: #c79a3e;
    --hero-ground: #0b0b0a;
    --strip-bg: #ffffff;
    --badge: #c9c9c9;
    --info-bg: #e9e9e9;
    --heading-blue: #1f6fb4;
    --body-text: #222222;
    --footer-bg: #d4d4d4;
    --footer-text: #333333;
  }
  * { margin: 0; padding: 0; box-sizing: border-box; }
  html, body { width: 1200px; height: 835px; overflow: hidden; background: var(--white); }
  body { position: relative; font-family: "Arimo", Arial, sans-serif; color: var(--body-text); }

  .hero {
    position: absolute; left: 0; top: 0; width: 1200px; height: 525px;
    background:
      radial-gradient(ellipse 520px 180px at 560px 470px, rgba(199,154,62,.55), transparent 70%),
      radial-gradient(ellipse 300px 140px at 1020px 420px, rgba(120,200,210,.35), transparent 70%),
      linear-gradient(180deg, var(--hero-top) 0%, var(--hero-mid) 55%, #2b3e5c 78%, var(--hero-ground) 100%);
  }
  .hero-headline {
    position: absolute; right: 213px; top: 92px; width: 620px;
    text-align: right; color: var(--white);
    font-family: "Arimo", Arial, sans-serif; font-weight: 400;
    font-size: 40px; line-height: 37px; letter-spacing: -0.3px;
  }
  .hero-intro {
    position: absolute; right: 216px; top: 231px; width: 600px;
    text-align: right; color: var(--white);
    font-family: "Questrial", Arial, sans-serif; font-size: 19px; line-height: 25px;
  }
  .slider-dots { position: absolute; left: 168px; top: 496px; display: flex; gap: 3px; }
  .slider-dots span { width: 8px; height: 8px; border-radius: 50%; background: var(--white); }
  .slider-dots span.is-current { background: var(--nav-active); }

  .topbar {
    position: absolute; left: 0; top: 0; width: 1200px; height: 38px;
    background: var(--nav-bg);
  }
  .brand {
    position: absolute; left: 150px; top: 0; width: 182px; height: 75px;
    background: var(--white); display: flex; align-items: center; justify-content: center; gap: 10px;
    font-family: "Open Sans", Arial, sans-serif; font-size: 22px; color: #555555; letter-spacing: 1px;
  }
  .brand-mark { width: 26px; height: 26px; background: #4aa7d8; }
  .main-nav { position: absolute; left: 0; top: 0; height: 38px; font-family: "Open Sans", Arial, sans-serif; font-size: 13.5px; }
  .main-nav a {
    position: absolute; top: 0; height: 38px; line-height: 38px;
    color: var(--nav-text); text-decoration: none; white-space: nowrap;
  }
  .main-nav a.is-active { background: var(--nav-active); color: var(--white); width: 51px; text-align: center; }
  .nav-email { display: flex; align-items: center; gap: 6px; color: var(--white) !important; }

  .partners {
    position: absolute; left: 0; top: 525px; width: 1200px; height: 80px; background: var(--strip-bg);
  }
  .partner-badge { position: absolute; background: var(--badge); border-radius: 3px; }

  .services {
    position: absolute; left: 0; top: 605px; width: 1200px; height: 193px; background: var(--info-bg);
  }
  .section-title { position: absolute; font-size: 18.5px; color: var(--heading-blue); font-weight: 400; }
  .role-list { position: absolute; list-style: none; font-size: 12.5px; line-height: 20px; }
  .role-list li::before { content: "•"; margin-right: 6px; }
  .role-list li.wrap { padding-left: 12px; text-indent: -12px; line-height: 15px; padding-top: 2px; }
  .positions-link { position: absolute; left: 150px; top: 150px; font-size: 14px; }
  .positions-link a { color: var(--heading-blue); text-decoration: none; }
  .contact-details { position: absolute; left: 888px; top: 69px; font-size: 11.5px; line-height: 15.5px; font-style: normal; }

  .site-footer {
    position: absolute; left: 0; top: 798px; width: 1200px; height: 37px; background: var(--footer-bg);
    font-size: 11px; color: var(--footer-text);
  }
  .footer-nav { position: absolute; left: 150px; top: 0; height: 37px; display: flex; align-items: center; gap: 10px; }
  .footer-nav a { color: var(--footer-text); text-decoration: none; }
  .footer-nav a.is-active { color: var(--heading-blue); }
  .footer-nav .sep { font-size: 9px; color: #555; }
  .copyright { position: absolute; right: 152px; top: 0; line-height: 37px; }
</style>
</head>
<body>

<section class="hero">
  <div role="img" aria-label="Night photograph of a power station with cooling tower, chimneys and construction cranes lit against a deep blue sky" style="position:absolute;inset:0;"></div>
  <h1 class="hero-headline">Australia’s number 1 Health,<br>Safety, Environment and<br>Quality recruitment group.</h1>
  <p class="hero-intro">TRVL-NINE is a Perth-based independent, specialised recruitment company with a focus on Health, Safety, Environment and Quality positions within the resources sector.</p>
  <div class="slider-dots"><span class="is-current"></span><span></span><span></span><span></span><span></span></div>
</section>

<header class="topbar">
  <nav class="main-nav">
    <a class="is-active" href="#" style="left:374px;">Home</a>
    <a href="#" style="left:443px;">About Us</a>
    <a href="#" style="left:520px;">Positions We Offer</a>
    <a href="#" style="left:645px;">Candidates</a>
    <a href="#" style="left:732px;">Employers</a>
    <a href="#" style="left:815px;">Contact Us</a>
    <a class="nav-email" href="#" style="left:901px;">
      <svg width="15" height="11" viewBox="0 0 15 11"><rect x="0.5" y="0.5" width="14" height="10" fill="#fff"/><path d="M0.5 0.5 L7.5 6 L14.5 0.5" fill="none" stroke="#3b3b3b" stroke-width="1.2"/></svg>
      perth@trvlnine.com.au
    </a>
  </nav>
</header>
<a class="brand" href="#"><span class="brand-mark"></span>TRVL-NINE</a>

<section class="partners" aria-label="Memberships and partners">
  <div class="partner-badge" style="left:216px;top:26px;width:86px;height:28px;"></div>
  <div class="partner-badge" style="left:343px;top:20px;width:106px;height:40px;"></div>
  <div class="partner-badge" style="left:490px;top:22px;width:92px;height:36px;"></div>
  <div class="partner-badge" style="left:638px;top:24px;width:155px;height:32px;"></div>
  <div class="partner-badge" style="left:838px;top:27px;width:150px;height:26px;"></div>
</section>

<section class="services">
  <h2 class="section-title" style="left:150px;top:27px;">Offering both contract and permanent placements, our areas of recruitment include</h2>
  <ul class="role-list" style="left:150px;top:69px;"><li>OHS Officers</li><li>Safety Advisors</li><li>Occupational Hygienists</li></ul>
  <ul class="role-list" style="left:309px;top:69px;"><li>Training Advisors</li><li>Training Superintendents</li><li>Training Managers</li></ul>
  <ul class="role-list" style="left:486px;top:69px;"><li>Quality Control Specialists</li><li>QAQC Engineers</li><li>Project Quality Managers</li></ul>
  <ul class="role-list" style="left:675px;top:69px;width:160px;"><li>Environmental Officers</li><li>Environmental Scientists</li><li class="wrap">Corporate Environmental Managers</li></ul>
  <p class="positions-link">For the complete list of positions we offer <a href="#">Click Here</a></p>

  <h2 class="section-title" style="left:885px;top:27px;">Contact Us</h2>
  <address class="contact-details">
    Suite 4, 77 Ridge Street<br>
    Subiaco Western Australia 6008<br>
    Phone: +61 (08) 5521 0930<br>
    Email: perth@trvlnine.com.au
  </address>
</section>

<footer class="site-footer">
  <nav class="footer-nav">
    <a class="is-active" href="#">Home</a><span class="sep">•</span>
    <a href="#">About Us</a><span class="sep">•</span>
    <a href="#">Positions We Offer</a><span class="sep">•</span>
    <a href="#">Candidates</a><span class="sep">•</span>
    <a href="#">Employers</a><span class="sep">•</span>
    <a href="#">Contact Us</a>
  </nav>
  <p class="copyright">© Copyright TRVL-NINE 2013. All Rights Reserved.</p>
</footer>

</body>
</html>
```